Vantorel Business Card

I want a business card for me and my employees.
On one side it must be in Greek and on the other side in English. The color must much the one of the logo

Target Market(s)

Customers that are looking for security and antipiracy advisors

Contact Information for Business Card

Title, Email, Phone, website , Mobile Address Zip code, city and country

Requirements
Must have
• The colors of our logo (the blue ones)

```html
<!DOCTYPE html>
<html lang="en">
<head>
<meta charset="utf-8">
<title>Vantorel Advisory – Business Card</title>
<link rel="stylesheet" href="https://fonts.googleapis.com/css2?family=Open+Sans:wght@400;600;700&family=Oswald:wght@500&display=swap">
<style>
  :root {
    --navy: #25215e;
    --navy-deep: #1f1b52;
    --navy-soft: #2e2a6b;
    --cream: #fbfbf2;
    --mist: #dcd9e2;
    --stage: #232323;
    --caption: #8a8a8a;
  }
  * { box-sizing: border-box; margin: 0; padding: 0; }
  html, body { width: 1200px; height: 780px; overflow: hidden; }
  body {
    background: var(--stage);
    font-family: "Open Sans", Arial, sans-serif;
    position: relative;
  }
  .side-caption {
    position: absolute;
    font-family: "Oswald", "Arial Narrow", sans-serif;
    font-weight: 500;
    font-size: 26px;
    letter-spacing: 0.5px;
    color: var(--caption);
    font-variant: small-caps;
    width: 380px;
    text-align: center;
  }
  .side-caption--greek { left: 650px; top: 28px; }
  .side-caption--english { left: 170px; top: 712px; }

  .card {
    position: absolute;
    top: 92px;
    width: 380px;
    height: 600px;
    border-radius: 30px;
    overflow: hidden;
    box-shadow: 0 14px 30px rgba(0,0,0,0.55);
  }
  .card--english { left: 170px; --ink: var(--navy); --body-ink: #1d1d1d; }
  .card--greek { left: 650px; --ink: #ffffff; --body-ink: #ffffff; }

  .card__backdrop { position: absolute; inset: 0; width: 100%; height: 100%; }

  .brand-mark {
    position: absolute;
    top: 28px;
    right: 24px;
    display: flex;
    align-items: center;
    gap: 8px;
    writing-mode: vertical-rl;
    transform: rotate(180deg);
    color: var(--ink);
    font-weight: 700;
    font-size: 26px;
    letter-spacing: 1px;
    line-height: 1;
  }
  .brand-mark__square { width: 28px; height: 28px; background: var(--ink); }
  .brand-mark__tagline { font-size: 16px; font-weight: 400; letter-spacing: 4px; }

  .card__decor-block {
    position: absolute;
    left: 28px; top: 70px;
    width: 170px; height: 170px;
  }
  .card--english .card__decor-block { background: var(--mist); }
  .card--greek .card__decor-block { background: var(--navy-soft); }

  .contact {
    position: absolute;
    left: 20px; right: 20px; top: 268px;
    text-align: center;
    color: var(--body-ink);
  }
  .contact__name { font-size: 28px; font-weight: 700; color: var(--ink); line-height: 1.15; }
  .contact__title { font-size: 15px; font-weight: 600; margin-top: 2px; }
  .contact__icons { display: flex; justify-content: center; gap: 6px; margin: 10px 0 6px; }
  .contact__icons svg { width: 22px; height: 22px; }
  .contact__line { font-size: 15px; line-height: 20px; }

  .address {
    position: absolute;
    left: 20px; right: 20px; top: 496px;
    text-align: center;
    color: var(--body-ink);
    font-size: 14px;
    line-height: 19px;
  }
  .address svg { width: 26px; height: 26px; display: block; margin: 0 auto 6px; }
</style>
</head>
<body>

<div class="side-caption side-caption--greek">Greek Language Side</div>
<div class="side-caption side-caption--english">English Language Side</div>

<!-- English side -->
<section class="card card--english">
  <svg class="card__backdrop" viewBox="0 0 380 600" preserveAspectRatio="none" aria-hidden="true">
    <defs>
      <linearGradient id="en-lower" x1="0" y1="0" x2="0" y2="1">
        <stop offset="0" stop-color="#d4d4cc"/>
        <stop offset="0.5" stop-color="#efefe8"/>
        <stop offset="1" stop-color="#f7f7f0"/>
      </linearGradient>
      <filter id="en-lift" x="-10%" y="-10%" width="120%" height="130%">
        <feDropShadow dx="0" dy="8" stdDeviation="8" flood-color="#000" flood-opacity="0.22"/>
      </filter>
    </defs>
    <rect width="380" height="600" fill="var(--cream)"/>
    <path d="M0,430 Q210,520 380,360 V600 H0 Z" fill="url(#en-lower)"/>
    <path d="M0,600 V565 Q190,470 380,430 V600 Z" fill="var(--cream)"/>
    <path d="M0,0 H380 V400 Q300,490 120,478 Q50,472 0,468 Z" fill="#f1f1ea" filter="url(#en-lift)"/>
    <path d="M0,0 H380 V330 Q300,460 110,460 Q50,460 0,455 Z" fill="var(--cream)" filter="url(#en-lift)"/>
  </svg>
  <div class="card__decor-block" aria-hidden="true"></div>
  <div class="brand-mark">
    <span class="brand-mark__square"></span>
    <span>VANTOREL</span>
    <span class="brand-mark__tagline">ADVISORY</span>
  </div>
  <div class="contact">
    <h1 class="contact__name">Daria Velinova</h1>
    <p class="contact__title">Managing Director</p>
    <div class="contact__icons" aria-hidden="true">
      <svg viewBox="0 0 24 24"><circle cx="12" cy="12" r="12" fill="var(--navy)"/><rect x="8.5" y="5.5" width="7" height="13" rx="1.5" fill="none" stroke="#fff" stroke-width="1.6"/></svg>
      <svg viewBox="0 0 24 24"><circle cx="12" cy="12" r="12" fill="var(--navy)"/><path d="M8 7l2.5 0 1 3-1.5 1.2a7 7 0 0 0 2.8 2.8L14 12.5l3 1v2.5c-5 .5-9.5-4-9-9z" fill="#fff"/></svg>
      <svg viewBox="0 0 24 24"><circle cx="12" cy="12" r="12" fill="var(--navy)"/><rect x="6" y="8" width="12" height="9" fill="none" stroke="#fff" stroke-width="1.6"/><path d="M6 8l6 5 6-5" fill="none" stroke="#fff" stroke-width="1.6"/></svg>
      <svg viewBox="0 0 24 24"><circle cx="12" cy="12" r="12" fill="var(--navy)"/><circle cx="12" cy="12" r="6" fill="none" stroke="#fff" stroke-width="1.5"/><path d="M6 12h12M12 6c-3 3-3 9 0 12M12 6c3 3 3 9 0 12" fill="none" stroke="#fff" stroke-width="1.2"/></svg>
    </div>
    <p class="contact__line">(555) 014-2758</p>
    <p class="contact__line">(555) 019-5555</p>
    <p class="contact__line">info@vantorel.com</p>
    <p class="contact__line">www.vantorel.com</p>
  </div>
  <div class="address">
    <svg viewBox="0 0 24 24" aria-hidden="true"><circle cx="12" cy="12" r="12" fill="var(--navy)"/><path d="M12 5a4 4 0 0 0-4 4c0 3 4 8 4 8s4-5 4-8a4 4 0 0 0-4-4z" fill="none" stroke="#fff" stroke-width="1.5"/><circle cx="12" cy="9" r="1.4" fill="#fff"/></svg>
    <p>418 Linden Ave. Suite 200</p>
    <p>Millbrook, TX 70412, USA</p>
  </div>
</section>

<!-- Greek side -->
<section class="card card--greek" lang="el">
  <svg class="card__backdrop" viewBox="0 0 380 600" preserveAspectRatio="none" aria-hidden="true">
    <defs>
      <filter id="gr-lift" x="-10%" y="-10%" width="120%" height="130%">
        <feDropShadow dx="0" dy="8" stdDeviation="8" flood-color="#000" flood-opacity="0.3"/>
      </filter>
    </defs>
    <rect width="380" height="600" fill="var(--navy)"/>
    <path d="M0,430 Q210,520 380,360 V600 H0 Z" fill="var(--navy-deep)"/>
    <path d="M0,600 V565 Q190,470 380,430 V600 Z" fill="var(--navy)"/>
    <path d="M0,0 H380 V400 Q300,490 120,478 Q50,472 0,468 Z" fill="#24205c" filter="url(#gr-lift)"/>
    <path d="M0,0 H380 V330 Q300,460 110,460 Q50,460 0,455 Z" fill="var(--navy)" filter="url(#gr-lift)"/>
  </svg>
  <div class="card__decor-block" aria-hidden="true"></div>
  <div class="brand-mark">
    <span class="brand-mark__square"></span>
    <span>VANTOREL</span>
    <span class="brand-mark__tagline">ADVISORY</span>
  </div>
  <div class="contact">
    <h2 class="contact__name">Ντάρια Βελίνοβα</h2>
    <p class="contact__title">Διευθύνουσα Σύμβουλος</p>
    <div class="contact__icons" aria-hidden="true">
      <svg viewBox="0 0 24 24"><circle cx="12" cy="12" r="12" fill="#fff"/><rect x="8.5" y="5.5" width="7" height="13" rx="1.5" fill="none" stroke="var(--navy)" stroke-width="1.6"/></svg>
      <svg viewBox="0 0 24 24"><circle cx="12" cy="12" r="12" fill="#fff"/><path d="M8 7l2.5 0 1 3-1.5 1.2a7 7 0 0 0 2.8 2.8L14 12.5l3 1v2.5c-5 .5-9.5-4-9-9z" fill="var(--navy)"/></svg>
      <svg viewBox="0 0 24 24"><circle cx="12" cy="12" r="12" fill="#fff"/><rect x="6" y="8" width="12" height="9" fill="none" stroke="var(--navy)" stroke-width="1.6"/><path d="M6 8l6 5 6-5" fill="none" stroke="var(--navy)" stroke-width="1.6"/></svg>
      <svg viewBox="0 0 24 24"><circle cx="12" cy="12" r="12" fill="#fff"/><circle cx="12" cy="12" r="6" fill="none" stroke="var(--navy)" stroke-width="1.5"/><path d="M6 12h12M12 6c-3 3-3 9 0 12M12 6c3 3 3 9 0 12" fill="none" stroke="var(--navy)" stroke-width="1.2"/></svg>
    </div>
    <p class="contact__line">(555) 014-2758</p>
    <p class="contact__line">(555) 019-5555</p>
    <p class="contact__line">info@vantorel.com</p>
    <p class="contact__line">www.vantorel.com</p>
  </div>
  <div class="address">
    <svg viewBox="0 0 24 24" aria-hidden="true"><circle cx="12" cy="12" r="12" fill="#fff"/><path d="M12 5a4 4 0 0 0-4 4c0 3 4 8 4 8s4-5 4-8a4 4 0 0 0-4-4z" fill="none" stroke="var(--navy)" stroke-width="1.5"/><circle cx="12" cy="9" r="1.4" fill="var(--navy)"/></svg>
    <p>Λεωφ. Λίντεν 418, Γραφείο 200</p>
    <p>Μίλμπρουκ, TX 70412, ΗΠΑ</p>
  </div>
</section>

</body>
</html>
```